Digital Mapping company needs a Proposal Cover Page template (Not Cover Letter).

We are looking for a new design of our proposal's front page. Sales people at Brindle Survey will use this new cover page when bidding for jobs, there will be Brindle Survey elements that will be set in stone but the potential client information will need to be adaptable/customizable (for example, we currently upload client logos to the home page of our proposals). I attach what we currently have.
Similar look and feel as our tradeshow booth pull up banners and website (www.brindlesurvey.example) (images of these are also attached). We would like to see designs that use similar colours: green/blue/teal/yellow/orange/red.

We have clients all over the world. We own state of the art mapping equipment (LiDAR). LiDAR and digital photography are acquired with our own Halvern 314 and other aircraft. The final proposal design should be recognizable and communicate: an experienced company, high quality, and state of the art mapping technology delivered worldwide.

Target Market(s)

Our clients are global and range from small business to large corporations. We have clients associated with Mining, Forestry, Engineering, Ecological and First Nations sectors (usually hired by Geologists & Engineers)

Industry/Entity Type

Technical Service

Font styles to use
Serif

Colors

Designer to choose colors to be used in the design.

Requirements
Must have
• Here are the basic items we would like to see on the cover page of our proposal:
• Our Company Name - Brindle Survey Ltd.
• Our Company Logo - attached
• Our Company contact information [customizable field as we have a few locations]
• Proposal service [customizable field to add]
• Proposal project name and location [customizable field to add]
• Proposal Job number [customizable field to add]
• Recipient company or individual and their logo [customizable field’s to add these]
• Date created [auto date]
• Subdued information/less focus on Brindle Survey’s name and contact information and a greater focus on the client and their project. Well chosen imagery will tie Brindle Survey’s services to the client’s needs without the client thinking about it. Good use of white space as well.
Nice to have
• Similar look and feel as our tradeshow booth pull up banners and website (images of these are attached). We would like to see designs that use similar colours: green/yellow/red/blue/teal.
Should not have
• Something that doesn't match or fit with our logo/website/pull up tradeshow banners that are attached. Something that doesn't include all the elements in our must have list.

```html
<!DOCTYPE html>
<html lang="en">
<head>
<meta charset="utf-8">
<title>Brindle Survey – Proposal Cover</title>
<link rel="stylesheet" href="https://fonts.googleapis.com/css2?family=Lato:wght@400;700;900&family=Oswald:wght@500;700&family=Arimo:ital,wght@1,700&display=swap">
<style>
  :root{
    --backdrop:#3a3a3a;
    --paper:#ffffff;
    --ink:#111111;
    --teal:#0890b4;
    --teal-deep:#066f8c;
    --teal-light:#29b4d2;
    --grey-light:#f2f2f3;
    --grey-mid:#c9c8ca;
    --terrain-blue:#2a8fb0;
    --terrain-green:#4c9a52;
    --terrain-yellow:#c6b626;
    --terrain-orange:#c0641c;
  }
  html,body{margin:0;width:1200px;height:1200px;overflow:hidden;background:var(--backdrop);}
  .cover{position:absolute;left:133px;top:0;width:934px;height:1200px;display:block;}
  .firm-name{font-family:'Lato',sans-serif;font-weight:900;font-size:33px;fill:var(--ink);}
  .service-title{font-family:'Arimo',sans-serif;font-style:italic;font-weight:700;font-size:33px;fill:var(--paper);}
  .client-title{font-family:'Oswald',sans-serif;font-weight:700;font-size:82px;fill:var(--paper);}
  .contact{font-family:'Lato',sans-serif;font-weight:400;font-size:16.5px;fill:var(--paper);}
  .client-logos{font-family:'Oswald',sans-serif;font-weight:500;font-size:26px;fill:var(--ink);}
  .brand-name{font-family:'Lato',sans-serif;font-weight:700;fill:var(--ink);}
</style>
</head>
<body>
<svg class="cover" viewBox="0 0 913 1173" xmlns="http://www.w3.org/2000/svg">
  <defs>
    <linearGradient id="grey-fold" x1="0" y1="0" x2="1" y2="0">
      <stop offset="0" stop-color="var(--grey-light)"/>
      <stop offset="1" stop-color="var(--grey-mid)"/>
    </linearGradient>
    <linearGradient id="terrain" x1="0" y1="0" x2="1" y2="0.2">
      <stop offset="0" stop-color="var(--terrain-blue)"/>
      <stop offset="0.45" stop-color="var(--terrain-green)"/>
      <stop offset="0.75" stop-color="var(--terrain-yellow)"/>
      <stop offset="1" stop-color="var(--terrain-orange)"/>
    </linearGradient>
  </defs>

  <!-- page -->
  <rect class="page" width="913" height="1173" fill="var(--paper)"/>

  <!-- header -->
  <polygon class="header-fold" points="0,0 270,0 603,427 0,427" fill="url(#grey-fold)"/>
  <rect class="header-rule" x="0" y="427" width="603" height="16" fill="var(--ink)"/>

  <g class="brand-mark">
    <circle cx="72" cy="98" r="34" fill="var(--teal)"/>
    <text class="brand-name" x="118" y="102" font-size="36">BRINDLE</text>
    <text class="brand-name" x="119" y="126" font-size="19" letter-spacing="7">SURVEY</text>
  </g>

  <text class="firm-name" x="868" y="149" text-anchor="end">BRINDLE SURVEY LTD</text>

  <polygon class="service-banner-tab" points="363,154 400,176 333,176" fill="var(--teal-deep)"/>
  <polygon class="service-banner" points="333,176 913,176 913,339 438,339" fill="var(--teal)"/>
  <g class="service-title" text-anchor="end">
    <text x="885" y="229">PROPOSAL TO [SERVICE</text>
    <text x="875" y="271">WE ARE PROVIDING] IN</text>
    <text x="875" y="313">[PROJECT LOCATION]</text>
  </g>

  <!-- project imagery -->
  <rect class="project-imagery" x="0" y="443" width="913" height="423" fill="url(#terrain)" role="img" aria-label="Colour-coded LiDAR elevation model of a mountain range"/>
  <polygon class="imagery-chevron" points="0,443 608,443 773,654 593,866 0,866" fill="var(--teal-light)" opacity="0.55"/>
  <polygon class="imagery-chevron-inner" points="0,443 280,443 450,654 270,866 0,866" fill="var(--teal-light)" opacity="0.35"/>
  <polygon class="imagery-notch" points="0,471 151,654 0,829" fill="var(--ink)"/>

  <g class="client-title">
    <text x="176" y="639">[COMPANY NAME].</text>
    <text x="176" y="722">[JOB NUMBER]</text>
  </g>

  <!-- footer -->
  <polygon class="footer-fold" points="268,866 593,866 358,1147 75,1147" fill="url(#grey-fold)"/>
  <polygon class="footer-panel" points="593,866 913,866 913,1173 0,1173 0,1147 358,1147" fill="var(--teal)"/>

  <text class="client-logos" x="52" y="1124">Logos</text>

  <g class="contact" text-anchor="end">
    <text x="885" y="1032">310 - 4480 Larchmont Road</text>
    <text x="885" y="1053">Ferncastle, BC, V0X 4T7</text>
    <text x="885" y="1074">Canada</text>
    <text x="885" y="1107">Office: +1 555.010.2468</text>
    <text x="885" y="1128">www.brindlesurvey.example</text>
  </g>
</svg>
</body>
</html>
```